Criação de Manual da Marca para Consultoria de Negócios
" Serviço de assinatura de informações para postos de combustíveis, em um mercado onde centavos são relevantes, a plataforma lumitra vendas vem ao encontro de atender o processo de precificação para os donos, gestores de postos de combustíveis. "

```html
<!DOCTYPE html>
<html lang="pt-BR">
<head>
<meta charset="utf-8">
<title>Manual da Marca — lumitra vendas</title>
<link rel="stylesheet" href="https://fonts.googleapis.com/css2?family=Orbitron:wght@700;900&family=Montserrat:wght@700;800&family=Open+Sans:wght@400;600;700&display=swap">
<style>
  :root{
    --navy:#083763;
    --orange:#ff6600;
    --paper:#f4f4f4;
    --grey-bg:#e4e4e4;
    --text:#5a5a5a;
    --light-navy:#1e5a92;
  }
  *{margin:0;padding:0;box-sizing:border-box}
  html,body{width:1200px;height:1200px;overflow:hidden}
  body{background:var(--grey-bg);font-family:"Open Sans",Arial,sans-serif;position:relative}

  .spread{position:absolute;left:60px;top:170px;width:1080px;height:740px;display:flex;box-shadow:0 10px 30px rgba(0,0,0,.18)}
  .page{position:relative;width:540px;height:740px;background:var(--paper);overflow:hidden}
  .page--left{border-right:1px solid #d6d6d6}
  .page-frame{position:absolute;left:0;top:0;width:540px;height:740px}

  .page-number{position:absolute;top:86px;font-family:"Montserrat",Arial,sans-serif;font-weight:800;font-size:34px;color:var(--orange)}
  .page--left .page-number{left:26px}
  .page--right .page-number{left:18px}
  .intro{position:absolute;top:76px;font-size:9.5px;line-height:1.5;color:var(--text)}
  .page--left .intro{left:100px;width:400px}
  .page--right .intro{left:92px;width:410px}

  .section-banner{position:absolute;top:170px;height:56px;background:var(--navy);color:#fff;font-family:"Montserrat",Arial,sans-serif;font-weight:800;font-size:26px;letter-spacing:1px;display:flex;align-items:center}
  .page--left .section-banner{left:0;width:240px;padding-left:60px;clip-path:polygon(0 0,88% 0,100% 100%,0 100%)}
  .page--right .section-banner{left:0;width:300px;padding-left:58px;clip-path:polygon(0 0,90% 0,100% 100%,0 100%)}
  .banner-edge{position:absolute;top:170px;height:56px;background:var(--orange)}
  .page--left .banner-edge{left:0;width:252px;clip-path:polygon(0 0,86% 0,100% 100%,0 100%);top:175px}
  .page--right .banner-edge{left:0;width:314px;clip-path:polygon(0 0,88% 0,100% 100%,0 100%);top:175px}

  .color-notes{position:absolute;left:34px;top:262px;width:190px;font-size:9.5px;line-height:1.5;color:var(--orange)}
  .color-notes p{margin-bottom:14px}
  .color-notes .muted{color:var(--navy)}

  .swatch{position:absolute;left:264px;width:48px;height:48px}
  .swatch--navy{top:268px;background:var(--navy)}
  .swatch--orange{top:340px;background:var(--orange)}
  .swatch-specs{position:absolute;left:326px;font-size:10px;line-height:1.35;color:var(--navy);font-weight:600}
  .swatch-specs--navy{top:268px}
  .swatch-specs--orange{top:340px}

  .tint-bar{position:absolute;left:264px;width:150px;height:42px}
  .tint-bar--navy{top:418px;background:linear-gradient(180deg,var(--navy) 0%,#3e6a96 45%,#c9d5e2 100%)}
  .tint-bar--orange{top:508px;background:linear-gradient(180deg,#ffd2b3 0%,#ff9a55 50%,var(--orange) 100%)}

  .brand-seal{position:absolute;left:64px;top:470px;width:120px;height:120px;border-radius:50%;border:6px solid var(--navy);background:#fff;display:flex;align-items:center;justify-content:center;text-align:center;font-family:"Montserrat",Arial,sans-serif;font-weight:800;font-size:15px;line-height:1.1;color:var(--navy);text-transform:uppercase}

  .type-lead{position:absolute;left:34px;top:250px;width:470px;font-size:9.5px;line-height:1.5;color:var(--orange)}
  .type-name{position:absolute;left:34px;top:298px;font-family:"Orbitron",Arial,sans-serif;font-weight:900;font-size:16px;color:var(--navy);letter-spacing:1px}
  .type-alphabet{position:absolute;left:34px;top:322px;width:470px;font-family:"Orbitron",Arial,sans-serif;font-weight:900;font-size:30px;line-height:1.05;color:var(--navy);letter-spacing:1px}
  .type-caption{position:absolute;left:34px;font-size:9px;line-height:1.45;color:var(--text)}
  .type-caption--one{top:396px;width:300px}
  .type-caption--two{top:474px;width:420px}
  .type-caption strong{color:var(--navy)}
  .type-digits{position:absolute;left:34px;top:426px;font-family:"Orbitron",Arial,sans-serif;font-weight:900;font-size:30px;color:var(--navy);letter-spacing:1px}

  .weight-grid{position:absolute;left:34px;top:498px;width:470px;display:grid;grid-template-columns:repeat(3,1fr);row-gap:6px;font-family:"Orbitron",Arial,sans-serif;font-size:20px;letter-spacing:1px}
  .weight-grid span{color:var(--orange)}
  .weight-grid .w-heavy{font-weight:900}
  .weight-grid .w-bold{font-weight:700}
  .weight-grid .w-outline{font-weight:700;color:#ff9a55}
  .weight-grid .w-soft{font-weight:700;color:#ffb585}

  .type-note{position:absolute;left:34px;top:580px;width:470px;font-size:9.5px;line-height:1.5;color:var(--text)}
  .type-note strong{color:var(--navy)}

  .brand-name{position:absolute;left:0;right:0;top:1010px;text-align:center;font-family:"Montserrat",Arial,sans-serif;font-weight:800;font-size:36px;color:var(--navy);text-transform:uppercase;letter-spacing:1px}
</style>
</head>
<body>
  <main class="spread">
    <section class="page page--left">
      <svg class="page-frame" viewBox="0 0 540 740" aria-hidden="true">
        <polygon points="0,0 540,0 540,44 0,44" fill="var(--navy)"/>
        <polygon points="220,44 540,44 540,58 200,58" fill="var(--orange)"/>
        <polygon points="0,44 200,44 180,58 0,58" fill="var(--light-navy)"/>
        <polygon points="0,690 330,690 350,706 0,706" fill="var(--orange)"/>
        <polygon points="0,706 540,706 540,740 0,740" fill="var(--navy)"/>
        <polygon points="370,690 540,690 540,706 390,706" fill="var(--light-navy)"/>
      </svg>
      <div class="page-number">06</div>
      <p class="intro">Lorem Ipsum is simply dummy text of the printing and typesetting industry. Lorem Ipsum has been the industry's standard dummy text ever since the 1500s, when an unknown printer took a galley of type and scrambled it to make a type specimen book used by many.</p>

      <div class="banner-edge"></div>
      <h2 class="section-banner">CORES</h2>

      <div class="color-notes">
        <p>As primeiras das cores do reconhecimento, que ajudam a criar uma distinção maior da marca em todos os meios do segmento. São elas: cinza e digitais laranja.</p>
        <p>As secundárias das cores de suporte, com um papel mais funcional, sendo que importante para criar uma harmonia com as primárias. São elas: cinza.</p>
        <p>As especificações ao lado devem apoiar a reprodução fiel das cores em todos os meios e suportes, impressos ou digitais.</p>
      </div>

      <div class="swatch swatch--navy"></div>
      <div class="swatch-specs swatch-specs--navy">CMYK: 100.84.34.25<br>RGB: 8.55.99<br>HEX: #083763</div>
      <div class="swatch swatch--orange"></div>
      <div class="swatch-specs swatch-specs--orange">CMYK: 0.74.100.0<br>RGB: 255.102.0<br>HEX: #FF6600</div>

      <div class="tint-bar tint-bar--navy"></div>
      <div class="tint-bar tint-bar--orange"></div>

      <div class="brand-seal">lumitra<br>vendas</div>
    </section>

    <section class="page page--right">
      <svg class="page-frame" viewBox="0 0 540 740" aria-hidden="true">
        <polygon points="0,0 540,0 540,44 0,44" fill="var(--navy)"/>
        <polygon points="0,44 330,44 310,58 0,58" fill="var(--orange)"/>
        <polygon points="350,44 540,44 540,58 330,58" fill="var(--light-navy)"/>
        <polygon points="200,690 540,690 540,706 180,706" fill="var(--orange)"/>
        <polygon points="0,706 540,706 540,740 0,740" fill="var(--navy)"/>
        <polygon points="0,690 160,690 140,706 0,706" fill="var(--light-navy)"/>
      </svg>
      <div class="page-number">07</div>
      <p class="intro">Lorem Ipsum is simply dummy text of the printing and typesetting industry. Lorem Ipsum has been the industry's standard dummy text ever since the 1500s, when an unknown printer took a galley of type and scrambled it to make a type specimen book used by many.</p>

      <div class="banner-edge"></div>
      <h2 class="section-banner">TIPOGRAFIA</h2>

      <p class="type-lead">Tipografia principal da marca, escolhida por seu traço largo e moderno, que transmite solidez e tecnologia. Deve ser aplicada em títulos, chamadas e destaques, sempre em caixa alta.</p>
      <div class="type-name">ZEBULON</div>
      <div class="type-alphabet">ABCDEFGHIJLMNOPQRS<br>TUVXZ</div>
      <p class="type-caption type-caption--one">Tipografia utilizada na palavra de destaque do logotipo e para títulos da papelaria básica, sites, materiais, vídeos, conteúdos e similares.</p>
      <div class="type-digits">1234567890</div>
      <p class="type-caption type-caption--two">Tipografia secundária aplicada em textos de apoio: <strong>MONTSERRAT E VARIAÇÕES</strong></p>

      <div class="weight-grid">
        <span class="w-heavy">ZEBULON</span>
        <span class="w-bold">ZEBULON</span>
        <span class="w-heavy">ZEBULON</span>
        <span class="w-outline">ZEBULON</span>
        <span class="w-bold">ZEBULON</span>
        <span class="w-soft">ZEBULON</span>
      </div>

      <p class="type-note"><strong>Observação:</strong> Não aplicar, seja em impressos ou meios digitais, variações da fonte fora deste manual. Todos os layouts devem seguir esta família, evitando conflitos visuais.</p>
    </section>
  </main>

  <div class="brand-name">lumitra vendas</div>
</body>
</html>
```